Rebrand of 3 bottle labels for nail polish brand

The task is to make a rebranding of our current gel nail polish bottle design. We have become one of the leading european nail polish brand, so we want to improve the quality of the label design to a more scandinavian and minimalistic bottle design, which stille has to be recognisable and unique.

We have attached a more detailed description of the rebranding instructions for our gel polish bottles called "bottle task".
Updates

The Labels should not be just Black and White as stated. But should be mainly Black and White and then some of our color as explained in the uploaded file.

Target Market(s)

Girls and women age 18-55 Northern Europe

Industry/Entity Type

Cosmetic/ Nail Gel Polish

Colors

Designer to choose only greyscale colors for use in the design.

Requirements
Must have
• See attched design instruction
Nice to have
• Moderne, Minimalist, Recognizable and Unique look
Should not have
• Too many elements, too busy design

```html
<!DOCTYPE html>
<html lang="en">
<head>
<meta charset="utf-8">
<title>Lumira gel polish labels</title>
<link rel="stylesheet" href="https://fonts.googleapis.com/css2?family=Montserrat:wght@300;400;500;600&display=swap">
<style>
  :root {
    --page: #f4f4f4;
    --label: #1e1e1e;
    --blush: #c49c94;
    --ink: #ffffff;
    --ink-soft: #d9d9d9;
    --mark: #8a8a8a;
  }
  * { margin: 0; padding: 0; box-sizing: border-box; }
  html, body { width: 667px; height: 1200px; overflow: hidden; }
  body {
    background: var(--page);
    font-family: "Montserrat", sans-serif;
    color: var(--ink);
    position: relative;
  }
  .label { position: absolute; background: var(--label); }
  .label > * { position: absolute; }
  .crop { width: 14px; height: 14px; border-color: var(--mark); border-style: solid; border-width: 0; }
  .crop-tl { left: -14px; top: -14px; border-right-width: 1px; border-bottom-width: 1px; }
  .crop-tr { right: -14px; top: -14px; border-left-width: 1px; border-bottom-width: 1px; }
  .crop-bl { left: -14px; bottom: -14px; border-right-width: 1px; border-top-width: 1px; }
  .crop-br { right: -14px; bottom: -14px; border-left-width: 1px; border-top-width: 1px; }

  .brand { font-weight: 300; letter-spacing: 0.5px; line-height: 1; white-space: nowrap; transform: translateX(-50%); }
  .centered { transform: translateX(-50%); text-align: center; white-space: nowrap; line-height: 1.15; }
  .band { left: 0; right: 0; background: var(--blush); }
  .leaf-mark { background: var(--blush); border-radius: 50% 50% 46% 46%; }

  /* small polish labels */
  .label-small { left: 119px; width: 429px; height: 123px; }
  .label-small .brand { left: 108px; top: 16px; font-size: 24px; }
  .label-small .product { left: 108px; top: 42px; font-size: 7px; font-weight: 500; letter-spacing: 0.3px; }
  .label-small .cure { left: 108px; top: 51px; font-size: 4.2px; color: var(--ink-soft); }
  .label-small .shade { left: 108px; top: 62px; font-size: 14px; font-weight: 500; }
  .label-small .leaf-mark { left: 9px; top: 46px; width: 56px; height: 44px; }
  .label-small .band { top: 93px; height: 12px; }
  .label-small .band-word { top: 94.5px; font-size: 7.5px; font-weight: 500; }
  .label-small .band-tag { left: 108px; }
  .label-small .band-web { left: 319px; font-weight: 600; }
  .label-small .vegan { left: 108px; top: 110px; font-size: 5.5px; color: var(--ink-soft); }
  .label-small .volume { right: 8px; top: 7px; font-size: 3.6px; font-weight: 600; }
  .label-small .info { left: 232px; top: 15px; width: 180px; font-size: 3.5px; line-height: 1.2; color: var(--ink-soft); }
  .info-head { display: block; text-align: center; font-weight: 600; color: var(--ink); }
  .label-small .origin { left: 320px; top: 85px; font-size: 3.5px; color: var(--ink-soft); }
  .label-small .address { left: 261px; top: 111px; font-size: 3.4px; color: var(--ink-soft); }
  .label-small .icons { left: 390px; top: 109px; width: 32px; height: 7px; }

  /* remover label */
  .label-large { left: 20px; top: 589px; width: 627px; height: 347px; }
  .label-large .brand { left: 156px; top: 64px; font-size: 37px; }
  .label-large .product { left: 157px; top: 150px; font-size: 9px; font-weight: 600; letter-spacing: 0.3px; }
  .label-large .shade { left: 157px; top: 201px; font-size: 31px; font-weight: 500; }
  .label-large .leaf-mark { left: 20px; top: 181px; width: 88px; height: 90px; border-radius: 50% 50% 50% 50% / 30% 30% 70% 70%; }
  .label-large .col { width: 118px; font-size: 5.2px; line-height: 1.28; color: var(--ink-soft); }
  .col-head { display: block; font-weight: 600; color: var(--ink); margin-bottom: 4px; }
  .label-large .col-eng-a { left: 336px; top: 40px; }
  .label-large .col-dk-a { left: 465px; top: 40px; }
  .label-large .col-eng-b { left: 336px; top: 129px; }
  .label-large .col-dk-b { left: 465px; top: 129px; }
  .label-large .ingredients { left: 336px; top: 174px; width: 260px; font-size: 5.2px; line-height: 1.3; color: var(--ink-soft); }
  .label-large .volume { left: 464px; top: 204px; font-size: 9px; font-weight: 300; color: var(--blush); }
  .label-large .icons { left: 444px; top: 224px; width: 40px; height: 14px; }
  .label-large .origin { left: 464px; top: 257px; font-size: 8.5px; font-weight: 300; }
  .label-large .address { left: 464px; top: 273px; font-size: 4.6px; color: var(--ink-soft); }
  .label-large .band { top: 284px; bottom: 0; left: 4px; }
  .label-large .web { left: 463px; top: 301px; font-size: 19px; font-weight: 600; }
</style>
</head>
<body>

<section class="label label-small" style="top:265px" aria-label="Color coat label">
  <span class="crop crop-tl"></span><span class="crop crop-tr"></span>
  <span class="crop crop-bl"></span><span class="crop crop-br"></span>
  <div class="leaf-mark" role="img" aria-label="Brand leaf symbol"></div>
  <div class="brand">lumira</div>
  <div class="product centered">COLOR COAT</div>
  <div class="cure centered">SOAK OFF UV/LED</div>
  <div class="shade centered">21</div>
  <div class="band"></div>
  <div class="band-word band-tag centered">color</div>
  <div class="band-word band-web centered">lumiranails.com</div>
  <div class="vegan centered">Vegan Formula</div>
  <div class="volume">15ml ℮ 0.5oz</div>
  <div class="info">
    <span class="info-head">DIRECTIONS FOR USE (ENG):</span>
    Lumira Color Coat must be applied in thin layers and cured in one of our Lumira Lamps.
    <span class="info-head">ANVENDELSE (DK):</span>
    Lumira Farver skal påføres i tynde lag og hærdes i en af vores Lumira Lamper.
    <span class="info-head">CAUTION (ENG):</span>
    Keep out of reach of children. Discontinue use if irritation occurs. Avoid direct sunlight or extreme exposure to LED or UV light.
    <span class="info-head">ADVARSEL (DK):</span>
    Opbevar utilgængeligt for børn. Stop din behandling, hvis produktet forudsager irritation. Undgå direkte sollys eller udsættelse for LED eller UV.
    <span class="info-head">INGREDIENTS:</span>
    Acrylates Copolymer, Acrylated Aliphatic Urethane, Cellulose Acetate Butanoate, Dimethicone, Ceresine, wax, Pigment Red, Carbon Black, Titanium dioxide, CI 77891
  </div>
  <div class="origin centered">Made in Germany</div>
  <div class="address">Nordvik Supply A/S - Havnegade 12, 1058 Copenhagen, Denmark</div>
  <svg class="icons" viewBox="0 0 32 7" aria-hidden="true" fill="none" stroke="#fff" stroke-width="0.6">
    <path d="M3 1 L6 6 L0 6 Z"/><rect x="10" y="1.5" width="5" height="4"/><circle cx="21" cy="3.5" r="2.5"/><path d="M27 6 L30 1 L31 6"/>
  </svg>
</section>

<section class="label label-small" style="top:424px" aria-label="Base coat label">
  <span class="crop crop-tl"></span><span class="crop crop-tr"></span>
  <span class="crop crop-bl"></span><span class="crop crop-br"></span>
  <div class="leaf-mark" role="img" aria-label="Brand leaf symbol in outline"></div>
  <div class="brand">lumira</div>
  <div class="product centered">BASE COAT</div>
  <div class="cure centered">SOAK OFF UV/LED</div>
  <div class="shade centered">01</div>
  <div class="band"></div>
  <div class="band-word band-tag centered">color</div>
  <div class="band-word band-web centered">lumiranails.com</div>
  <div class="vegan centered">Vegan Formula</div>
  <div class="volume">15ml ℮ 0.5oz</div>
  <div class="info">
    <span class="info-head">DIRECTIONS FOR USE (ENG):</span>
    Lumira Base Coat must be applied in thin layers and cured in one of our Lumira Lamps.
    <span class="info-head">ANVENDELSE (DK):</span>
    Lumira Base Coat skal påføres i tynde lag og hærdes i en af vores Lumira Lamper.
    <span class="info-head">CAUTION (ENG):</span>
    Keep out of reach of children. Discontinue use if irritation occurs. Avoid direct sunlight or extreme exposure to LED or UV light.
    <span class="info-head">ADVARSEL (DK):</span>
    Opbevar utilgængeligt for børn. Stop din behandling, hvis produktet forudsager irritation. Undgå direkte sollys eller udsættelse for LED eller UV.
    <span class="info-head">INGREDIENTS:</span>
    Acrylates Copolymer, Acrylated Aliphatic Urethane, Cellulose Acetate Butanoate, Dimethicone, Ceresine, wax, Pigment Red, Carbon Black, Titanium dioxide, CI 77891
  </div>
  <div class="origin centered">Made in Europe</div>
  <div class="address">Nordvik Supply A/S - Havnegade 12, 1058 Copenhagen, Denmark</div>
  <svg class="icons" viewBox="0 0 32 7" aria-hidden="true" fill="none" stroke="#fff" stroke-width="0.6">
    <path d="M3 1 L6 6 L0 6 Z"/><rect x="10" y="1.5" width="5" height="4"/><circle cx="21" cy="3.5" r="2.5"/><path d="M27 6 L30 1 L31 6"/>
  </svg>
</section>

<section class="label label-large" aria-label="Gel polish remover label">
  <span class="crop crop-tl"></span><span class="crop crop-tr"></span>
  <span class="crop crop-bl"></span><span class="crop crop-br"></span>
  <div class="brand">lumira</div>
  <div class="product centered">GEL POLISH<br>REMOVER</div>
  <div class="leaf-mark" role="img" aria-label="Brand leaf symbol, half filled"></div>
  <div class="shade centered">12</div>
  <div class="col col-eng-a">
    <span class="col-head">DIRECTIONS FOR USE (ENG):</span>
    To remove the Lumira, soak a lint free wipe with the Lumira Polish Remover, place the saturated wipe on the nail and wrap each nail in foil for 15 minutes. Remove the foil and peel off the gel polish remover. Re-apply if needed. We recommend that you moisturise your nails after this treatment
  </div>
  <div class="col col-dk-a">
    <span class="col-head">ANVENDELSESGUIDE (DK):</span>
    For at fjerne Lumira, skal du væde en fnugfri wipe ind i Lumira Neglelakfjerner, hvorefter du placere din fnugfri wipe på neglen og klemmer den fast i 15 minutter med sølvpapir og negleklips. Fjern herefter foliet og skrab din gellak af med en eglebåndsskubber. Gentag hvis nødvendigt. Vi anbefaler neglеolie efter din behandling.
  </div>
  <div class="col col-eng-b">
    <span class="col-head">CAUTION (ENG):</span>
    Keep out of the reach of children Discontinue use if sensitivity or irritation occurs
  </div>
  <div class="col col-dk-b">
    <span class="col-head">ADVARSEL (DK):</span>
    Opbevares utilgængeligt for børn Stop din behandling hvis følsomhed eller irritation opstår
  </div>
  <div class="ingredients">
    <span class="col-head">INGREDIENTS:</span>
    Ethyl acetate, n-butyl acetate, Methyl Ethyl ketone, Acetone, Isopropyl alcohol, glycerin
  </div>
  <div class="volume centered">120 ml ℮ 4 fl.oz</div>
  <svg class="icons" viewBox="0 0 40 14" aria-hidden="true" fill="none" stroke="#fff" stroke-width="0.9">
    <rect x="2" y="5" width="11" height="7"/><path d="M2 5 L12 1"/>
    <path d="M28 3 L31 7 L25 7 Z M33 7 L35 11 L29 11 M26 9 L24 12 L29 12"/>
  </svg>
  <div class="origin centered">Made in Europe</div>
  <div class="address centered">Nordvik Supply A/S - Havnegade 12, 1058 Copenhagen, Denmark</div>
  <div class="band"></div>
  <div class="web centered">lumiranails.com</div>
</section>

</body>
</html>
```